Brackenmoor - Healthcare Brochure - B2B

We need a new brochure design, we're satisfied with the copy but were just looking for complete overhaul of the design. Please see an example of the old design attached. It was just a template we filled out.
Requirements
Nice to have
- The second attachment is an example of a style we like

```html
<!DOCTYPE html>
<html lang="en">
<head>
<meta charset="utf-8">
<title>Brackenmoor – Post-Acute Care Brochure</title>
<link rel="stylesheet" href="https://fonts.googleapis.com/css2?family=Lexend:wght@400;500;600&family=Montserrat:ital,wght@0,300;0,400;0,500;1,600&family=Caveat:wght@500&display=swap">
<style>
  :root{
    --page:#cdd5db;
    --navy:#1b2b45;
    --slate:#3f5a78;
    --ink:#1f2f49;
    --body:#3c4656;
    --muted:#7c8898;
    --accent:#1f6fb8;
    --sky:#dbeaf6;
    --mist:#eef3f7;
    --silver:#c9d3dd;
    --photo-warm:#c9b8a8;
    --photo-cool:#b9c9d8;
    --white:#ffffff;
    --head:"Lexend", sans-serif;
    --text:"Montserrat", sans-serif;
    --script:"Caveat", cursive;
  }
  *{box-sizing:border-box;margin:0;padding:0}
  html,body{width:720px;height:1200px;overflow:hidden}
  body{background:var(--page);font-family:var(--text);color:var(--body);position:relative}

  .spread{position:absolute;left:20px;width:680px;height:529px;overflow:hidden;background:var(--white)}
  .spread--outside{top:40px;background:linear-gradient(180deg,var(--sky) 0%,#f1f6fa 45%,var(--white) 70%)}
  .spread--inside{top:631px;background:var(--white)}
  .layer{position:absolute;inset:0}

  .brand{position:absolute;display:flex;align-items:center;gap:6px;font-family:var(--head);font-weight:400;color:var(--ink);letter-spacing:.04em;text-transform:uppercase}
  .brand__dot{width:12px;height:12px;border-radius:50%;background:var(--ink)}

  .photo-ring{position:absolute;border-radius:50%;border:4px solid var(--white);box-shadow:0 0 0 2px #b8cde0;background:linear-gradient(160deg,#e9eef3,var(--photo-warm) 60%,#8c97a6)}

  h2.contact-title{position:absolute;left:41px;top:312px;font-family:var(--head);font-weight:600;font-size:20px;color:var(--ink)}
  .contact-intro{position:absolute;left:42px;top:346px;width:150px;font-size:8px;line-height:12px}
  .contact-item{position:absolute;left:41px;display:flex;gap:6px}
  .contact-item__icon{width:22px;height:22px;border-radius:50%;background:var(--accent);display:flex;align-items:center;justify-content:center;flex:none}
  .contact-item__label{font-family:var(--head);font-weight:500;font-size:10px;color:var(--accent);line-height:12px}
  .contact-item__text{font-size:7.5px;line-height:11px;color:var(--ink)}

  .quote{position:absolute;left:247px;top:336px;width:182px;height:92px;border:1px solid #9fb1c4;border-radius:6px;padding:20px 12px 0 13px;font-size:7.6px;line-height:12px;color:var(--ink)}
  .quote__mark{position:absolute;left:12px;top:-13px;width:25px;height:25px;border-radius:50%;background:var(--slate);color:var(--white);font-family:var(--head);font-size:20px;line-height:30px;text-align:center}

  .cover-text{position:absolute;left:450px;top:336px;width:230px;text-align:center}
  .cover-text__tag{font-family:var(--script);font-size:17px;color:#6fa3d2}
  .cover-text__title{font-family:var(--head);font-weight:600;font-size:22px;line-height:25px;color:var(--ink);margin-top:4px}
  .cover-text__sub{font-size:12px;color:#4a5566;margin-top:6px}
  .cover-text__note{font-size:8.5px;line-height:11px;color:var(--muted);width:160px;margin:2px auto 0}

  .contact-bar{position:absolute;top:479px;height:50px;border-radius:12px 12px 0 0;color:var(--white);text-align:center;padding-top:12px}
  .contact-bar--dark{background:var(--navy)}
  .contact-bar--slate{background:var(--slate)}
  .contact-bar__lead{font-size:7.8px;font-weight:300;letter-spacing:.02em}
  .contact-bar__phone{display:flex;align-items:center;justify-content:center;gap:3px;font-weight:500;font-size:10px;letter-spacing:.06em;margin-top:3px}

  .about{position:absolute;left:30px;top:346px;width:190px}
  .about__title{font-family:var(--head);font-weight:600;font-size:20px;color:var(--ink)}
  .about__body{font-size:8px;line-height:10.2px;color:#58606c;margin-top:6px}
  .about__pull{font-size:7.4px;line-height:10px;font-style:italic;font-weight:600;color:var(--ink);margin-top:11px}

  .vision{position:absolute;left:262px;top:140px;width:182px}
  .vision__title{font-family:var(--head);font-weight:500;font-size:20px;color:var(--ink)}
  .vision__body{font-size:7.8px;line-height:10.2px;color:var(--muted);margin-top:5px}

  .feature{position:absolute;width:180px}
  .feature__head{display:flex;align-items:center;gap:6px}
  .feature__icon{width:36px;height:36px;border-radius:50%;flex:none;background:var(--white);border:3px solid var(--slate);display:flex;align-items:center;justify-content:center}
  .feature__icon--grey{border-color:#8e9aa7}
  .feature__icon span{width:14px;height:14px;border:1.5px solid var(--ink);border-radius:3px}
  .feature__title{font-family:var(--head);font-weight:500;font-size:11px;line-height:13px;color:var(--ink)}
  .feature__text{font-size:7.8px;line-height:10px;color:var(--ink);margin-top:5px;padding-left:3px}
</style>
</head>
<body>

<!-- Outside spread -->
<section class="spread spread--outside" aria-label="Brochure outside spread">
  <svg class="layer" width="680" height="529" viewBox="0 0 680 529" aria-hidden="true">
    <rect x="224" y="0" width="226" height="529" fill="#eef3f8" opacity=".6"/>
    <path d="M450 0H680V529H450Z" fill="#f7f9fb" opacity=".7"/>
    <path d="M450 300C540 340 620 330 680 300V316C620 350 540 355 450 318Z" fill="var(--silver)"/>
  </svg>

  <svg class="layer" width="680" height="529" viewBox="0 0 680 529" role="img" aria-label="Photo of a patient and a nurse reviewing a tablet together">
    <path d="M0 145C60 110 150 105 224 128V286C150 290 60 290 0 298Z" fill="url(#g-warm)"/>
    <defs>
      <linearGradient id="g-warm" x1="0" y1="0" x2="1" y2="1">
        <stop offset="0" stop-color="#dfe6ec"/><stop offset=".55" stop-color="#b9aea4"/><stop offset="1" stop-color="#8f9aa6"/>
      </linearGradient>
      <linearGradient id="g-cool" x1="0" y1="0" x2="1" y2="1">
        <stop offset="0" stop-color="#eef2f5"/><stop offset=".6" stop-color="#c8cfd6"/><stop offset="1" stop-color="#a9b6c3"/>
      </linearGradient>
    </defs>
  </svg>
  <svg class="layer" width="680" height="529" viewBox="0 0 680 529" role="img" aria-label="Photo of a team of doctors gathered around a laptop">
    <path d="M450 112C520 110 600 120 680 70V300C620 335 540 335 470 292C462 288 456 282 450 276Z" fill="url(#g-cool2)"/>
    <defs>
      <linearGradient id="g-cool2" x1="0" y1="0" x2="1" y2="1">
        <stop offset="0" stop-color="#eef2f5"/><stop offset=".6" stop-color="#cdd3da"/><stop offset="1" stop-color="#a7b4c1"/>
      </linearGradient>
    </defs>
  </svg>
  <div class="photo-ring" style="left:264px;top:160px;width:152px;height:152px" role="img" aria-label="Photo of a doctor checking on a seated patient"></div>

  <div class="brand" style="left:268px;top:86px;font-size:19px"><span class="brand__dot"></span>Brackenmoor</div>
  <div class="brand" style="left:500px;top:86px;font-size:19px"><span class="brand__dot"></span>Brackenmoor</div>

  <h2 class="contact-title">Get in Touch!</h2>
  <p class="contact-intro">Join us in transforming post-acute care. Let's make every patient's transition a story of success.</p>
  <div class="contact-item" style="top:398px">
    <span class="contact-item__icon"><svg width="10" height="12" viewBox="0 0 10 12"><path d="M5 0.5C2.6 0.5 1 2.2 1 4.3 1 7.2 5 11.5 5 11.5S9 7.2 9 4.3C9 2.2 7.4 0.5 5 0.5Z" fill="#fff"/><circle cx="5" cy="4.3" r="1.5" fill="var(--accent)"/></svg></span>
    <div><div class="contact-item__label">Location</div><div class="contact-item__text">48 Larkfield Rd, Ste 210, Halden,<br>MA, 02190</div></div>
  </div>
  <div class="contact-item" style="top:442px">
    <span class="contact-item__icon"><svg width="11" height="11" viewBox="0 0 11 11"><rect x="2.5" y="0.5" width="6" height="3.5" fill="none" stroke="#fff"/><rect x="0.5" y="4" width="10" height="6" rx="1" fill="none" stroke="#fff"/><line x1="3" y1="7" x2="8" y2="7" stroke="#fff"/></svg></span>
    <div><div class="contact-item__label">Fax</div><div class="contact-item__text">555-014-7735</div></div>
  </div>

  <div class="quote"><span class="quote__mark">“</span>Our process is simple, fast, and most importantly: effective. One call, and we take it from there. From your healthcare facility to their home, we're there every step of the way.</div>
  <div class="brand" style="left:265px;top:446px;font-size:18px"><span class="brand__dot"></span>Brackenmoor</div>

  <div class="cover-text">
    <div class="cover-text__tag">Bridging Gaps. Improving Lives</div>
    <div class="cover-text__title">Revolutionizing<br>Post-Acute Care</div>
    <div class="cover-text__sub">One Patient at a Time</div>
    <div class="cover-text__note">Because every patient deserves a seamless recovery</div>
  </div>

  <div class="contact-bar contact-bar--dark" style="left:15px;width:201px">
    <div class="contact-bar__lead">For more information Please Contact</div>
    <div class="contact-bar__phone"><svg width="9" height="9" viewBox="0 0 10 10"><circle cx="5" cy="5" r="5" fill="var(--accent)"/><path d="M3.4 2.6 4.3 3.6 3.8 4.3C4.2 5.1 4.9 5.8 5.7 6.2L6.4 5.7 7.4 6.6 6.8 7.5C4.9 7.3 2.7 5.1 2.5 3.2Z" fill="#fff"/></svg>555-014-2290</div>
  </div>
  <div class="contact-bar contact-bar--slate" style="left:232px;width:207px">
    <div class="contact-bar__lead">For more information Please Contact</div>
    <div class="contact-bar__phone"><svg width="9" height="9" viewBox="0 0 10 10"><circle cx="5" cy="5" r="5" fill="var(--accent)"/><path d="M3.4 2.6 4.3 3.6 3.8 4.3C4.2 5.1 4.9 5.8 5.7 6.2L6.4 5.7 7.4 6.6 6.8 7.5C4.9 7.3 2.7 5.1 2.5 3.2Z" fill="#fff"/></svg>555-014-2290</div>
  </div>
  <div class="contact-bar contact-bar--dark" style="left:459px;width:209px">
    <div class="contact-bar__lead">For more information Please Contact</div>
    <div class="contact-bar__phone"><svg width="9" height="9" viewBox="0 0 10 10"><circle cx="5" cy="5" r="5" fill="var(--accent)"/><path d="M3.4 2.6 4.3 3.6 3.8 4.3C4.2 5.1 4.9 5.8 5.7 6.2L6.4 5.7 7.4 6.6 6.8 7.5C4.9 7.3 2.7 5.1 2.5 3.2Z" fill="#fff"/></svg>555-014-2290</div>
  </div>
</section>

<!-- Inside spread -->
<section class="spread spread--inside" aria-label="Brochure inside spread">
  <svg class="layer" width="680" height="529" viewBox="0 0 680 529" aria-hidden="true">
    <defs>
      <linearGradient id="g-sky" x1="0" y1="0" x2="1" y2="1">
        <stop offset="0" stop-color="#cfe4f4"/><stop offset=".6" stop-color="#e7f0f7"/><stop offset="1" stop-color="#f4f7fa"/>
      </linearGradient>
      <linearGradient id="g-mid" x1="0" y1="0" x2="0" y2="1">
        <stop offset="0" stop-color="#ffffff"/><stop offset="1" stop-color="#eef2f6"/>
      </linearGradient>
    </defs>
    <rect width="680" height="529" fill="url(#g-sky)"/>
    <path d="M0 220C120 170 200 140 300 90C420 40 560 40 680 40V529H0Z" fill="#fff"/>
    <rect x="232" y="120" width="228" height="409" fill="url(#g-mid)"/>
    <path d="M420 60C500 35 600 35 680 50V125C600 125 500 110 420 60Z" fill="#e2e9ef"/>
    <path d="M0 200C50 240 90 250 140 240V262C90 270 40 258 0 235Z" fill="#8597ad"/>
  </svg>
  <div style="position:absolute;left:20px;top:40px;width:190px;height:270px;border-radius:0 0 95px 95px;background:linear-gradient(180deg,#e6d4c6 0%,#f4f1ee 45%,#dfe5ea 100%)" role="img" aria-label="Photo of a smiling doctor in a white coat with arms crossed"></div>

  <div class="brand" style="left:30px;top:314px;font-size:16px"><span class="brand__dot"></span>Brackenmoor</div>
  <div class="about">
    <h2 class="about__title">About Brackenmoor</h2>
    <p class="about__body">At Brackenmoor, we don't just bridge the gap. We transform the journey into a smooth, seamless experience, from the moment a patient discharges from your facility until their appointment with a primary care physician. For Medicare beneficiaries, that's life-changing</p>
    <p class="about__pull">Delivering personalized, seamless care that empowers patients, reduces readmissions, and ensures smooth recovery from healthcare facility to home</p>
  </div>

  <div class="vision">
    <h2 class="vision__title">Our Vision</h2>
    <p class="vision__body">To make the healthcare experience for every patient as fluid, efficient, and compassionate as possible. Through cutting-edge care and seamless coordination, we ensure patients recover faster, stay healthier, and never lose sight of their well being.</p>
  </div>

  <div class="feature" style="left:257px;top:258px">
    <div class="feature__head"><span class="feature__icon"><span></span></span><span class="feature__title">Seamless Transition</span></div>
    <p class="feature__text">We ensure smooth facility-to home transitions with no gaps in care, prioritizing patient outcomes.</p>
  </div>
  <div class="feature" style="left:257px;top:344px">
    <div class="feature__head"><span class="feature__icon feature__icon--grey"><span></span></span><span class="feature__title">Prescription Refills</span></div>
    <p class="feature__text">We handle refills for non controlled prescriptions, ensuring your patients have what they need to recover.</p>
  </div>
  <div class="feature" style="left:257px;top:430px">
    <div class="feature__head"><span class="feature__icon feature__icon--grey"><span></span></span><span class="feature__title">Reduced<br>Readmission Risk</span></div>
    <p class="feature__text">We minimize readmission risk with proactive care, enhancing outcomes and supporting value based care goals.</p>
  </div>

  <div class="feature" style="left:478px;top:140px">
    <div class="feature__head"><span class="feature__icon"><span></span></span><span class="feature__title">VNA Order Sign-Off</span></div>
    <p class="feature__text">We sign off on VNA orders, streamlining the process and ensuring seamless home care coordination.</p>
  </div>
  <div class="feature" style="left:478px;top:225px">
    <div class="feature__head"><span class="feature__icon feature__icon--grey"><span></span></span><span class="feature__title">Streamlined Referral<br>Process</span></div>
    <p class="feature__text">Easily refer patients with a fast, simple process that ensures seamless transitions in care.</p>
  </div>
  <div class="feature" style="left:478px;top:316px">
    <div class="feature__head"><span class="feature__icon feature__icon--grey"><span></span></span><span class="feature__title">Patient Education</span></div>
    <p class="feature__text">Empowering patients with information to make informed decisions about their health.</p>
  </div>

  <svg class="layer" width="680" height="529" viewBox="0 0 680 529" role="img" aria-label="Photo of a doctor listening to a patient's back with a stethoscope">
    <defs>
      <linearGradient id="g-exam" x1="0" y1="0" x2="1" y2="1">
        <stop offset="0" stop-color="#eef0f2"/><stop offset=".55" stop-color="#c9ccd2"/><stop offset="1" stop-color="#b2586a"/>
      </linearGradient>
    </defs>
    <path d="M479 420C560 410 620 400 673 394V529H540C510 495 490 460 479 420Z" fill="url(#g-exam)"/>
  </svg>
</section>

</body>
</html>
```